Oru Loft Business Card

We need a business card designed for a a company called "Oru Loft". We offer consulting, coaching and training to business leaders and coaches (across the world) using the latest findings in neuroscience, social and emotional intelligence and positive psychology. The final design should communicate the use of brain science to create sustainable relationships.

The card should be doublesided. The logo is attached and names and titles will be provided to the successful designer. Thank you.

```html
<!DOCTYPE html>
<html lang="en">
<head>
<meta charset="utf-8">
<title>Oru Loft Business Card</title>
<link href="https://fonts.googleapis.com/css2?family=Open+Sans:wght@400;600;800&display=swap" rel="stylesheet">
<style>
  :root {
    --backdrop: #eef0f2;
    --paper: #ffffff;
    --brand-blue: #0b88c4;
    --brand-green: #b5d40f;
    --accent-green: #1fa33a;
    --ink: #1c1c1c;
  }
  * { box-sizing: border-box; margin: 0; padding: 0; }
  html, body { width: 1200px; height: 900px; overflow: hidden; }
  body {
    background: var(--backdrop);
    font-family: "Open Sans", Arial, sans-serif;
    position: relative;
  }
  .card {
    position: absolute;
    left: 270px;
    width: 660px;
    height: 377px;
    background: var(--paper);
    overflow: hidden;
    box-shadow: 0 4px 14px rgba(0,0,0,0.12);
  }
  .card--front { top: 48px; }
  .card--back { top: 475px; }
  .card__waves { position: absolute; inset: 0; width: 100%; height: 100%; }
  .brand {
    position: absolute;
    display: flex;
    align-items: center;
    gap: 10px;
    color: var(--brand-blue);
    font-weight: 800;
    font-size: 40px;
    letter-spacing: 1px;
    white-space: nowrap;
  }
  .brand__dot {
    width: 22px; height: 22px; border-radius: 50%;
    background: var(--brand-blue);
  }
  .card--front .brand { top: 70px; left: 50%; transform: translateX(-50%); }
  .card--back .brand { top: 88px; left: 48px; }
  .website-band {
    position: absolute;
    left: 150px; top: 290px;
    color: var(--paper);
    font-size: 22px;
    letter-spacing: 2px;
  }
  .divider {
    position: absolute;
    left: 340px; top: 40px;
    width: 3px; height: 190px;
    background: var(--accent-green);
  }
  .person { position: absolute; right: 52px; top: 48px; text-align: right; color: var(--ink); }
  .person__name { font-size: 31px; font-weight: 400; line-height: 1.1; }
  .person__title { font-size: 19px; }
  .contact { position: absolute; left: 366px; top: 148px; list-style: none; color: var(--ink); font-size: 19px; }
  .contact__item { display: flex; align-items: center; gap: 12px; height: 28px; }
  .contact__icon { width: 18px; height: 18px; flex: none; }
</style>
</head>
<body>

<section class="card card--front" aria-label="Card front">
  <svg class="card__waves" viewBox="0 0 660 377" preserveAspectRatio="none" aria-hidden="true">
    <path d="M0,238 C220,212 440,280 660,377 L0,377 Z" fill="var(--brand-blue)"/>
    <path d="M0,226 C220,200 450,262 660,352" fill="none" stroke="var(--brand-green)" stroke-width="7"/>
  </svg>
  <div class="brand"><span class="brand__dot"></span>Oru Loft</div>
  <p class="website-band">www.oruloft.com</p>
</section>

<section class="card card--back" aria-label="Card back">
  <svg class="card__waves" viewBox="0 0 660 377" preserveAspectRatio="none" aria-hidden="true">
    <path d="M0,245 C200,230 480,270 625,377 L0,377 Z" fill="var(--brand-blue)"/>
    <path d="M0,232 C210,214 500,252 648,377" fill="none" stroke="var(--brand-green)" stroke-width="7"/>
  </svg>
  <div class="brand"><span class="brand__dot"></span>Oru Loft</div>
  <div class="divider"></div>
  <div class="person">
    <p class="person__name">Marlo Keane</p>
    <p class="person__title">CEO</p>
  </div>
  <ul class="contact">
    <li class="contact__item">
      <svg class="contact__icon" viewBox="0 0 20 20" aria-hidden="true">
        <circle cx="10" cy="10" r="9" fill="none" stroke="var(--accent-green)" stroke-width="1.5"/>
        <path d="M6.5,5.5 l2,-0.5 1,2.5 -1.2,1 a6,6 0 0 0 3,3 l1,-1.2 2.5,1 -0.5,2 c-4,0.5 -8.5,-4 -7.8,-7.8z" fill="var(--accent-green)"/>
      </svg>
      (555) 014-2736
    </li>
    <li class="contact__item">
      <svg class="contact__icon" viewBox="0 0 20 20" aria-hidden="true">
        <rect x="2" y="5" width="16" height="11" fill="none" stroke="var(--accent-green)" stroke-width="1.5"/>
        <path d="M2,5 L10,11 L18,5" fill="none" stroke="var(--accent-green)" stroke-width="1.5"/>
      </svg>
      marlo@oruloft.com
    </li>
    <li class="contact__item">
      <svg class="contact__icon" viewBox="0 0 20 20" aria-hidden="true">
        <circle cx="10" cy="10" r="8.5" fill="none" stroke="var(--accent-green)" stroke-width="1.5"/>
        <ellipse cx="10" cy="10" rx="3.5" ry="8.5" fill="none" stroke="var(--accent-green)" stroke-width="1.3"/>
        <path d="M1.5,10 H18.5 M3,5.5 H17 M3,14.5 H17" stroke="var(--accent-green)" stroke-width="1.3"/>
      </svg>
      www.oruloft.com
    </li>
  </ul>
</section>

</body>
</html>
```